Reed & Vale NC grand opening (for BILLBOARD)

Advertising the grand opening of our cannabis/hemp shop in NC. We will sell all things hemp (flower, cartridges, disposables, edibles, creams, lotions, pet products etc...)

Requirements
Must have
• include, open starting Aug 1, but grand opening Aug 15th.
Nice to have
• Difference slogan ideas "Save some cash, buy our grass" "Find your perfect high at Reed & Vale cannabis store" "Experience Nature's Gift: Reed & Vale Cannabis Store"

```html
<!DOCTYPE html>
<html lang="en">
<head>
<meta charset="utf-8">
<title>Reed &amp; Vale Grand Opening Billboard</title>
<link rel="stylesheet" href="https://fonts.googleapis.com/css2?family=Montserrat:wght@600;700&family=Oswald:wght@500&display=swap">
<style>
  :root {
    --navy: #0f1034;
    --green: #7dc242;
    --green-dark: #0f6a3c;
    --white: #ffffff;
    --stripe: #eef0f7;
    --page-top: #f1f1f1;
    --page-bottom: #c6c6c6;
    --ink: #111111;
  }
  * { margin: 0; padding: 0; box-sizing: border-box; }
  html, body { width: 1200px; height: 1200px; overflow: hidden; }
  body {
    background: linear-gradient(160deg, var(--page-top), var(--page-bottom));
    font-family: "Montserrat", sans-serif;
    position: relative;
  }
  .billboard {
    position: absolute; left: 56px; top: 407px;
    width: 1088px; height: 320px;
    background: var(--navy);
    overflow: hidden;
    box-shadow: 0 8px 18px rgba(0,0,0,0.25);
  }
  .billboard-bg { position: absolute; inset: 0; }
  .megaphone {
    position: absolute; top: 135px; width: 225px; height: 185px;
    background: linear-gradient(135deg, #eef1fb, #7dc242);
    border-radius: 40px 40px 0 0;
  }
  .megaphone--left { left: 21px; }
  .megaphone--right { right: 21px; }
  .brand-name {
    position: absolute; left: 0; right: 0; top: 52px;
    text-align: center; font-weight: 700; font-size: 62px;
    color: var(--green); letter-spacing: -1px; line-height: 1;
  }
  .slogan {
    position: absolute; left: 0; right: 0; top: 122px;
    text-align: center; font-weight: 700; font-size: 26px;
    color: var(--white); letter-spacing: 0.5px;
  }
  .slogan em { font-style: normal; color: var(--green); }
  .big-date {
    position: absolute; top: 160px;
    font-family: "Oswald", sans-serif; font-weight: 500;
    font-size: 86px; line-height: 1; color: var(--green);
  }
  .big-date sup {
    font-size: 28px; color: var(--white); vertical-align: top;
    position: relative; top: 10px; margin-left: 4px;
  }
  .date-first { left: 321px; }
  .date-grand { left: 720px; }
  .month-badge {
    position: absolute; top: 176px; width: 51px; height: 20px;
    background: var(--green-dark); color: var(--white);
    font-weight: 700; font-size: 14px; line-height: 20px;
    text-align: center; border-radius: 2px;
  }
  .event-label {
    position: absolute; font-weight: 700; font-size: 28px;
    color: var(--white); line-height: 1;
  }
  .divider {
    position: absolute; left: 543px; top: 159px; width: 1px; height: 80px;
    background: var(--white);
  }
  .amp {
    position: absolute; left: 536px; top: 189px; padding: 2px 0;
    background: var(--navy); color: var(--green);
    font-family: "Oswald", sans-serif; font-size: 20px; line-height: 1;
  }
  .pin {
    position: absolute; left: 528px; top: 242px;
  }
  .address {
    position: absolute; left: 423px; top: 271px; width: 242px; height: 30px;
    border: 1.5px solid var(--green-dark); border-radius: 4px;
    color: var(--white); font-weight: 600; font-size: 16px;
    line-height: 27px; text-align: center; letter-spacing: 1px;
  }
  .size-label {
    position: absolute; left: 0; right: 0; top: 755px;
    text-align: center; font-weight: 700; font-size: 34px; color: var(--ink);
  }
  .size-label small { font-size: 20px; }
</style>
</head>
<body>
  <section class="billboard">
    <svg class="billboard-bg" viewBox="0 0 1088 320" width="1088" height="320">
      <g class="corner-left">
        <polygon fill="var(--stripe)" points="0,0 446,0 277,80 283,42 28,167 32,123 0,140"/>
        <polygon fill="var(--green)" points="0,0 404,0 277,80 283,20 27,165 32,113 0,128"/>
      </g>
      <g class="corner-right" transform="translate(1088,0) scale(-1,1)">
        <polygon fill="var(--stripe)" points="0,0 446,0 277,80 283,42 28,167 32,123 0,140"/>
        <polygon fill="var(--green)" points="0,0 404,0 277,80 283,20 27,165 32,113 0,128"/>
      </g>
    </svg>

    <div class="megaphone megaphone--left" role="img" aria-label="Green and white megaphone illustration pointing right"></div>
    <div class="megaphone megaphone--right" role="img" aria-label="Green and white megaphone illustration pointing left"></div>

    <h1 class="brand-name">Reed &amp; Vale</h1>
    <p class="slogan">Save Some <em>Cash</em>, Buy Our <em>Grass</em></p>

    <div class="big-date date-first">1<sup>ST</sup></div>
    <span class="month-badge" style="left:390px">AUG</span>
    <span class="event-label" style="left:447px; top:174px">Open</span>
    <span class="event-label" style="left:388px; top:208px">Starting</span>

    <span class="divider"></span>
    <span class="amp">&amp;</span>

    <span class="event-label" style="left:560px; top:174px">Grand</span>
    <span class="month-badge" style="left:658px">AUG</span>
    <span class="event-label" style="left:560px; top:208px">Opening</span>
    <div class="big-date date-grand">15<sup>TH</sup></div>

    <svg class="pin" width="32" height="32" viewBox="0 0 32 32">
      <circle cx="16" cy="16" r="16" fill="var(--green)"/>
      <path d="M16 8a5 5 0 0 0-5 5c0 4 5 9 5 9s5-5 5-9a5 5 0 0 0-5-5z" fill="none" stroke="var(--white)" stroke-width="1.5"/>
      <circle cx="16" cy="13" r="1.8" fill="none" stroke="var(--white)" stroke-width="1.3"/>
      <path d="M10 22l-2 3h16l-2-3" fill="none" stroke="var(--white)" stroke-width="1.3"/>
    </svg>
    <div class="address">Exit 4B Maplewood Rd</div>
  </section>

  <p class="size-label">1088<small>px</small> W x 320<small>px</small> H</p>
</body>
</html>
```